Winery label for Birchfall Ridge Winery

New Winery on 265 acre farm in West Central Indiana, presently 10 acres of vineyard increasing to 16 acres in spring of 2018. An Estate Winery as wine will be produced from vine to bottle onsite. An event profit center is planned. Beautiful property with abundant wildlife including a large population of American Eagles , waterfowl, upland game, Marrow Fen Canal system traverses the property , abundant Native American artifacts on site , property bordered by Pell Run and its mouth at the Dunmoor River. Entered the Tolvane Open Vintners Trial in July 2016 as an amateur and won three medals for BRW Wine.
Updates
I am changing my BIRCHFALL RIDGE WINERY with the deer. It has a potential copywriter infringement. How can I send a jpeg pic to all designers ? .
Target Market(s)
100 mile radius, upscale easily recognized brand-label-logo, onsite sale, events,wine club distribution
Industry/Entity Type
Farm
Colors
Designer to choose colors to be used in the design.
Requirements
Must have
- eye appeal and brand recognition
Nice to have
- Read project description
Should not have
- Brand rights conflicts

```html
<!DOCTYPE html>
<html lang="es">
<head>
<meta charset="utf-8">
<title>Birchfall Ridge Winery – Etiqueta</title>
<link rel="stylesheet" href="https://fonts.googleapis.com/css2?family=Bebas+Neue&family=Montserrat:wght@400;600&family=Cormorant+Garamond:wght@500&display=swap">
<style>
  :root {
    --backdrop: #2a1409;
    --label-black: #0b0b0c;
    --label-band: #151517;
    --gold: #d8b45a;
    --gold-light: #f4dc93;
    --gold-dark: #8a6a22;
    --ink-light: #eae6dc;
    --pattern: #1b1c20;
  }
  * { margin: 0; padding: 0; box-sizing: border-box; }
  html, body { width: 1200px; height: 1059px; overflow: hidden; }
  body {
    background: radial-gradient(ellipse at 50% 40%, #4a220d 0%, var(--backdrop) 55%, #0e0603 100%);
    position: relative;
    font-family: "Montserrat", sans-serif;
  }

  /* Neck label */
  .neck-label {
    position: absolute; left: 120px; top: 190px;
    width: 220px; height: 225px;
    background: var(--label-black);
    display: flex; flex-direction: column; align-items: center; justify-content: center;
    gap: 26px;
  }
  .neck-label .brand-mark { font-size: 17px; }
  .neck-label .product-word { font-size: 62px; }

  /* Main label */
  .main-label {
    position: absolute; left: 430px; top: 190px;
    width: 620px; height: 680px;
    background: var(--label-black);
    overflow: hidden;
  }
  .gold-band { position: absolute; left: 0; width: 100%; }
  .gold-band.top { top: 0; height: 70px; }
  .gold-band.bottom { bottom: 0; height: 45px; }

  .medallion {
    position: absolute; left: 160px; top: 80px;
    width: 300px; height: 300px; border-radius: 50%;
    background: radial-gradient(circle, var(--pattern) 0%, #121316 60%, var(--label-black) 72%);
  }

  .maker-line {
    position: absolute; top: 105px; width: 100%;
    display: flex; justify-content: center; align-items: center; gap: 10px;
    color: var(--gold-light);
    font-weight: 600; font-size: 24px; letter-spacing: 2px;
  }
  .maker-line .diamond { width: 8px; height: 8px; background: var(--gold); transform: rotate(45deg); }

  .product-word {
    font-family: "Bebas Neue", sans-serif;
    color: var(--gold);
    background: linear-gradient(180deg, var(--gold-light) 0%, var(--gold) 55%, var(--gold-dark) 100%);
    -webkit-background-clip: text; background-clip: text;
    -webkit-text-fill-color: transparent;
    letter-spacing: 4px; line-height: 1;
  }
  .main-label .product-word {
    position: absolute; top: 140px; width: 100%; text-align: center;
    font-size: 138px;
  }

  .emblem {
    position: absolute; left: 250px; top: 275px; width: 120px; height: 75px;
    background: radial-gradient(ellipse at 50% 70%, #5a4520 0%, #2a2418 55%, transparent 75%);
  }

  .story-band {
    position: absolute; left: 0; top: 355px; width: 100%; height: 175px;
    background: var(--label-band);
  }
  .divider {
    position: absolute; left: 85px; width: 450px; height: 1px;
    background: linear-gradient(90deg, transparent, var(--gold) 20%, var(--gold) 80%, transparent);
  }
  .divider.upper { top: 10px; }
  .divider.lower { top: 162px; }
  .divider-knot {
    position: absolute; left: 292px; top: 0; width: 36px; height: 20px;
    border: 2px solid var(--gold); border-radius: 50%; background: var(--label-band);
  }
  .story {
    position: absolute; top: 48px; width: 100%; text-align: center;
    color: var(--ink-light); font-size: 17px; line-height: 26px;
  }

  .brand-mark {
    font-family: "Cormorant Garamond", serif; font-weight: 500;
    color: var(--ink-light); display: flex; align-items: center; gap: 8px;
  }
  .brand-mark .dot { width: 12px; height: 12px; border-radius: 50%; background: var(--ink-light); }
  .main-label .brand-mark {
    position: absolute; top: 535px; left: 0; width: 100%; justify-content: center;
    font-size: 26px;
  }

  .spec-row {
    position: absolute; top: 590px; left: 70px; right: 70px;
    display: flex; justify-content: space-between; align-items: baseline;
    color: var(--ink-light);
    font-family: "Cormorant Garamond", serif; font-size: 26px;
  }
  .spec-row .web { font-family: "Montserrat", sans-serif; font-weight: 600; font-size: 18px; }
</style>
</head>
<body>

<section class="neck-label">
  <div class="brand-mark"><span class="dot"></span>Birchfall Ridge</div>
  <div class="product-word">WINERY</div>
</section>

<section class="main-label">
  <svg class="gold-band top" viewBox="0 0 620 70" preserveAspectRatio="none" aria-hidden="true">
    <defs>
      <linearGradient id="goldSheen" x1="0" y1="0" x2="1" y2="0">
        <stop offset="0" stop-color="#8a6a22"/>
        <stop offset="0.5" stop-color="#f4dc93"/>
        <stop offset="1" stop-color="#8a6a22"/>
      </linearGradient>
    </defs>
    <polygon points="0,0 620,0 620,20 310,52 0,20" fill="#0b0b0c"/>
    <polygon points="120,0 500,0 310,22" fill="url(#goldSheen)"/>
    <polyline points="0,28 310,60 620,28" fill="none" stroke="#d8b45a" stroke-width="2"/>
  </svg>

  <div class="medallion" role="img" aria-label="Faint circular ornamental pattern behind the title"></div>

  <div class="maker-line"><span class="diamond"></span>BIRCHFALL RIDGE<span class="diamond"></span></div>
  <h1 class="product-word">WINERY</h1>

  <div class="emblem" role="img" aria-label="Small torch and star emblem in gold"></div>

  <div class="story-band">
    <div class="divider upper"></div>
    <div class="divider-knot"></div>
    <p class="story">Resultado de mezcla de los mas finos rones<br>dominicanos envejecidos de manera natural<br>en barricas de roble</p>
    <div class="divider lower"></div>
  </div>

  <div class="brand-mark"><span class="dot"></span>Birchfall Ridge</div>

  <div class="spec-row">
    <span class="volume">500 ML</span>
    <span class="web">www.birchfallridge.com</span>
    <span class="abv">30% VOL</span>
  </div>

  <svg class="gold-band bottom" viewBox="0 0 620 45" preserveAspectRatio="none" aria-hidden="true">
    <defs>
      <linearGradient id="goldSheenLow" x1="0" y1="0" x2="1" y2="0">
        <stop offset="0" stop-color="#8a6a22"/>
        <stop offset="0.5" stop-color="#f4dc93"/>
        <stop offset="1" stop-color="#8a6a22"/>
      </linearGradient>
    </defs>
    <polygon points="0,28 310,8 620,28 620,45 0,45" fill="url(#goldSheenLow)"/>
  </svg>
</section>

</body>
</html>
```